Delivery Performance Dashboard for Web Portal

We need you to design a dashboard for our web portal. We deliver sand and stone to construction jobsites. The attached screenshot is from our current web portal dashboard . It shows how much material has been delivered from an order.

Dump trucks will deliver multiple loads during the day and the dispatcher uses the dashboard to monitor if they need to add more trucks or less trucks to fulfill the order. An example would be, I need to ship 1,000 tons of sand to a jobsite and I plan to use 10 trucks during the day and that it will take 10 hours of hauling to complete the job. After 5 hours of hauling (50% the day is over), I should have delivered 500 tons of sand (50% of the order). But maybe there is a lot of traffic, and I only have delivered 300 tons. The dashboard will show that I am behind schedule and I might need to add 2 more trucks to the job.

Industry/Entity Type

Construction

Font styles to use
Sans Serif

Requirements
Must have
• We need a progress bar showing how much material has been delivered, how much material was requested to be delivered total and how much material should have been delivered at the current time. The goal is to show the user if the deliveries are ahead or behind the expected pace and why.
Nice to have
• The icons for plant, driving and jobsite show if the actual times have exceeded or beaten the planned times. Maybe you have other ideas to show the user if the trucks are sitting longer on the jobsite, at the plant to get loaded or driving to and from the jobsite.

```html
<!DOCTYPE html>
<html lang="en">
<head>
<meta charset="utf-8">
<title>Delivery Performance Dashboard</title>
<link href="https://fonts.googleapis.com/css2?family=Montserrat:wght@500;600;700&display=swap" rel="stylesheet">
<style>
:root{
  --blue:#5b9bff;
  --bg:#f6f7fb;
  --card:#ffffff;
  --ink:#111111;
  --muted:#3a3a3a;
  --rule:#d4d6e0;
  --track:#ececf0;
  --red:#ff1a1a;
  --icon:#aab0bc;
}
*{box-sizing:border-box;margin:0;padding:0}
html,body{width:1200px;height:695px;overflow:hidden}
body{position:relative;background:var(--bg);font-family:"Montserrat",sans-serif;color:var(--ink)}
.abs{position:absolute;white-space:nowrap}
.topbar{left:0;top:0;width:1200px;height:53px;background:var(--card)}
.menu-btn{left:22px;top:21px}
.search{left:975px;top:26px}
.bell{left:1015px;top:24px}
.bell-dot{left:1029px;top:19px;width:6px;height:6px;border-radius:50%;background:var(--blue)}
.user{right:90px;top:26px;text-align:right;line-height:1}
.user-name{font-size:7px;font-weight:700;color:#222}
.user-role{font-size:5px;font-weight:700;color:var(--blue);margin-top:2px}
.avatar{left:1115px;top:11px;width:42px;height:42px;border-radius:50%;background:radial-gradient(circle at 50% 40%,#c9a48a,#6f6a5e)}
.sidebar{left:0;top:53px;width:60px;height:642px;background:var(--blue)}
.side-icon{left:22px}
.side-active{left:56px;top:47px;width:4px;height:51px;background:#fff}
.card{background:var(--card)}
.order-card{left:105px;top:90px;width:295px;height:432px}
.order-card .title{left:29px;top:46px;font-size:27px;font-weight:700;color:var(--blue)}
.label{left:29px;font-size:17px;font-weight:600;color:var(--blue)}
.value{left:29px;font-size:16px;font-weight:600;color:var(--muted);line-height:23px}
.cycle-card{left:431px;top:90px;width:711px;height:432px}
.cycle-card .title{left:55px;top:44px;font-size:26px;font-weight:700;color:var(--blue)}
.avg{left:339px;top:44px;display:flex;align-items:center;gap:16px;font-size:22px;font-weight:600}
.row{left:58px;width:592px;height:40px;display:flex;align-items:center;font-size:20px;font-weight:600}
.row svg{position:absolute;left:0}
.row span{white-space:nowrap}
.row .name{position:absolute;left:47px}
.row .plan{position:absolute;left:285px}
.row .actual{position:absolute;left:497px}
.rule{left:58px;width:592px;height:1px;background:var(--rule)}
.tons-card{left:105px;top:550px;width:665px;height:111px}
.tons-card h2{left:31px;top:26px;font-size:23px;font-weight:600}
.meta{top:70px;font-size:10px;font-weight:600}
.meta.amount{left:32px;color:#8a8f9a}
.meta.window{right:39px;color:var(--blue)}
.track{left:32px;top:97px;width:599px;height:6px;border-radius:3px;background:var(--track)}
.fill{left:32px;top:97px;width:360px;height:6px;border-radius:3px;background:var(--blue)}
.remain-card{left:804px;top:550px;width:337px;height:111px}
.remain-card .clock{left:20px;top:41px}
.remain-card h2{left:65px;top:40px;font-size:25px;font-weight:500}
.hrs{right:23px;top:49px;font-size:15px;font-weight:600;color:var(--blue)}
.trucks{right:23px;top:75px;display:flex;align-items:center;gap:8px;font-size:17px;font-weight:700;color:var(--red)}
.pager{right:17px;top:672px;display:flex;align-items:center;gap:6px;font-size:10px;font-weight:700;color:#333}
</style>
</head>
<body>
<header class="abs topbar">
  <svg class="abs menu-btn" width="20" height="14" viewBox="0 0 20 14"><g stroke="#5b9bff" stroke-width="2"><line x1="0" y1="2" x2="20" y2="2"/><line x1="0" y1="7" x2="20" y2="7"/><line x1="0" y1="12" x2="20" y2="12"/></g></svg>
  <svg class="abs search" width="16" height="16" viewBox="0 0 16 16" fill="none" stroke="#aab0bc" stroke-width="1.6"><circle cx="7" cy="7" r="5.5"/><line x1="11" y1="11" x2="15" y2="15"/></svg>
  <svg class="abs bell" width="16" height="18" viewBox="0 0 16 18" fill="none" stroke="#aab0bc" stroke-width="1.6"><path d="M3 13V8a5 5 0 0 1 10 0v5l1.5 2h-13z"/><path d="M6.5 17h3"/></svg>
  <div class="abs bell-dot"></div>
  <div class="abs user"><div class="user-name">Marten Olde</div><div class="user-role">Manager</div></div>
  <div class="abs avatar" role="img" aria-label="User profile photo"></div>
</header>

<nav class="abs sidebar">
  <div class="abs side-active"></div>
  <svg class="abs side-icon" style="top:66px" width="16" height="16" viewBox="0 0 16 16" fill="none" stroke="#fff" stroke-width="1.4"><path d="M2 7l6-5 6 5v7H2z"/><path d="M6.5 14v-4h3v4"/></svg>
  <svg class="abs side-icon" style="top:125px" width="16" height="16" viewBox="0 0 16 16" fill="none" stroke="#fff" stroke-width="1.4"><path d="M8 1.5l2 4.3 4.6.5-3.4 3.1 1 4.6L8 11.6 3.8 14l1-4.6L1.4 6.3 6 5.8z"/></svg>
  <svg class="abs side-icon" style="top:181px" width="16" height="16" viewBox="0 0 16 16" fill="none" stroke="#fff" stroke-width="1.4"><path d="M9 3H3v11h10V8"/><circle cx="13" cy="3" r="2" fill="#fff" stroke="none"/></svg>
  <svg class="abs side-icon" style="top:245px" width="16" height="16" viewBox="0 0 16 16" fill="none" stroke="#fff" stroke-width="1.4"><path d="M1.5 3h5l1.5 2h6.5v8.5h-13z"/></svg>
  <svg class="abs side-icon" style="top:311px" width="16" height="16" viewBox="0 0 16 16" fill="none" stroke="#fff" stroke-width="1.4"><circle cx="8" cy="6" r="3.5"/><path d="M2 15c0-3.5 2.7-5.5 6-5.5s6 2 6 5.5z"/></svg>
</nav>

<section class="abs card order-card">
  <h1 class="abs title">Order : 17746</h1>
  <div class="abs label" style="top:109px">Customer</div>
  <div class="abs value" style="top:139px">Halvern Builders<br>North Division</div>
  <div class="abs label" style="top:208px">Status</div>
  <div class="abs value" style="top:237px">Accepted</div>
  <div class="abs label" style="top:290px">Orgin</div>
  <div class="abs value" style="top:318px">Ridgeway Aggregate Plant</div>
  <div class="abs label" style="top:364px">Destination</div>
  <div class="abs value" style="top:392px">KTRW - R12 from mm 12 - 33</div>
</section>

<section class="abs card cycle-card">
  <h2 class="abs title">Order 117746</h2>
  <div class="abs avg">
    <svg width="32" height="24" viewBox="0 0 32 24" fill="none" stroke="#5b9bff" stroke-width="2.4"><path d="M2 8h27M23 2l6 6"/><path d="M30 17H3M9 23l-6-6"/></svg>
    <span>Avg Cycle Time: 2hr 27min</span>
  </div>

  <div class="abs row" style="top:133px">
    <svg width="36" height="32" viewBox="0 0 36 32" fill="#5b9bff"><path d="M0 32V4h5v12l9-6v6l9-6v6l9-6V0h4v32z"/><g fill="#fff"><rect x="8" y="24" width="3" height="3"/><rect x="14" y="24" width="3" height="3"/><rect x="20" y="24" width="3" height="3"/></g></svg>
    <span class="name">Plant (min)</span><span class="plan">Planed: 30</span><span class="actual">Actual: 33</span>
  </div>
  <div class="abs rule" style="top:192px"></div>

  <div class="abs row" style="top:208px">
    <svg width="36" height="26" viewBox="0 0 36 26" fill="#5b9bff"><path d="M0 2h22v17H0z"/><path d="M23 8h7l5 6v5H23z"/><circle cx="7" cy="21" r="4"/><circle cx="28" cy="21" r="4"/><g fill="#fff"><circle cx="7" cy="21" r="1.5"/><circle cx="28" cy="21" r="1.5"/></g></svg>
    <span class="name">Driving (min)</span><span class="plan">Planed: 60</span><span class="actual">Actual: 83</span>
  </div>
  <div class="abs rule" style="top:267px"></div>

  <div class="abs row" style="top:284px">
    <svg width="36" height="30" viewBox="0 0 36 30"><path d="M21 0a10 10 0 0 0-10 10c0 7 10 20 10 20s10-13 10-20A10 10 0 0 0 21 0z" fill="#5b9bff"/><circle cx="21" cy="10" r="3.5" fill="#fff"/></svg>
    <span class="name">Jobsite (min)</span><span class="plan">Planed: 30</span><span class="actual">Actual: 30</span>
  </div>
  <div class="abs rule" style="top:343px"></div>

  <div class="abs row" style="top:360px">
    <svg width="36" height="24" viewBox="0 0 36 24" fill="#5b9bff"><path d="M0 10h8l3-5h6v12H0z"/><path d="M18 12h18v5H18z"/><path d="M22 2h12v9H22z"/><circle cx="5" cy="19" r="3.5"/><circle cx="14" cy="19" r="3.5"/><circle cx="28" cy="20" r="3"/></svg>
    <span class="name">Equipment (min)</span><span class="actual">Actual</span>
  </div>
</section>

<section class="abs card tons-card">
  <h2 class="abs">Tons</h2>
  <div class="abs meta amount">722.57 /1500</div>
  <div class="abs meta window">7:30AM - 5:00PM</div>
  <div class="abs track"></div>
  <div class="abs fill"></div>
</section>

<section class="abs card remain-card">
  <svg class="abs clock" width="30" height="30" viewBox="0 0 30 30" fill="none" stroke="#111" stroke-width="2.2"><circle cx="15" cy="15" r="13"/><path d="M15 7v8h-5"/></svg>
  <h2 class="abs">Remaining</h2>
  <div class="abs hrs">+1:25 HRS</div>
  <div class="abs trucks">
    <svg width="20" height="14" viewBox="0 0 20 14" fill="#111"><path d="M0 1h12v9H0z"/><path d="M13 4h4l3 3v3h-7z"/><circle cx="4" cy="11.5" r="2.3"/><circle cx="16" cy="11.5" r="2.3"/></svg>
    <span>-31</span>
  </div>
</section>

<div class="abs pager">
  <span>1-3 OF 3</span>
  <svg width="14" height="8" viewBox="0 0 14 8" fill="none" stroke="#333" stroke-width="1.4"><path d="M4 1L1 4l3 3M10 1l3 3-3 3"/></svg>
</div>
</body>
</html>
```